DOG DAYCARE BILLBOARD

Design a bold exciting billboard that can be read easily from a distance! Our goal is brand awareness and showcasing the services we offer (Boarding, Grooming, Daycare, and Training.
we would like to see examples with the phrase "your best friend's best day". Our name Bright Meadow Canine Activity Center (or just Bright Meadow might work better and could be bigger) and the services we provide.
(there are two examples of what we like included in the pictures)
you can find more information o our website at pawplayhub@mailnest.example.

```html
<!DOCTYPE html>
<html lang="en">
<head>
<meta charset="utf-8">
<title>Bright Meadow Billboard</title>
<link href="https://fonts.googleapis.com/css2?family=Poppins:wght@400;600;700&family=Nunito:wght@800&display=swap" rel="stylesheet">
<style>
  :root {
    --ink: #0b0b0b;
    --panel-dark: #262626;
    --lime: #dcd300;
    --white: #ffffff;
    --stage: #d9d9d9;
  }
  * { margin: 0; padding: 0; box-sizing: border-box; }
  html, body { width: 1081px; height: 1200px; overflow: hidden; }
  body { background: var(--stage); position: relative; font-family: "Poppins", sans-serif; }

  .billboard {
    position: absolute; left: 40px; top: 350px; width: 1000px; height: 500px;
    background: linear-gradient(90deg, #000 0%, #1c1c1c 45%, var(--panel-dark) 100%);
    overflow: hidden;
  }
  .billboard > * { position: absolute; }

  .sun { left: 0; top: 0; width: 1000px; height: 500px; }

  .hero-photo {
    left: 545px; top: 30px; width: 380px; height: 355px;
    border-radius: 30px;
    background: radial-gradient(ellipse at 55% 45%, #c9a27a 0%, #b8905f 40%, #a9d08a 72%, rgba(220,211,0,0) 100%);
    opacity: .9;
  }

  .headline { left: 0; top: 0; width: 520px; font-weight: 700; line-height: 1; }
  .headline span { position: absolute; white-space: nowrap; }
  .headline .line-1 { left: 121px; top: 22px; font-size: 64px; color: var(--white); }
  .headline .line-2 { left: 41px; top: 80px; font-size: 89px; color: var(--lime); }
  .headline .line-3 { left: 167px; top: 166px; font-size: 63px; color: var(--white); }

  .services-title { left: 44px; top: 232px; font-size: 26px; font-weight: 400; color: var(--white); line-height: 1.4; }
  .services-rule { left: 44px; top: 277px; width: 324px; height: 2px; background: #cfcfcf; }

  .services { left: 44px; top: 285px; width: 360px; list-style: none;
    display: grid; grid-template-columns: 183px auto; grid-auto-rows: 36px;
    font-family: "Nunito", sans-serif; font-weight: 800; font-size: 26px; color: var(--lime); }
  .services li { display: flex; align-items: center; gap: 7px; line-height: 1; }
  .services svg { width: 18px; height: 18px; flex: none; }

  .footer-bands { left: 0; top: 0; width: 1000px; height: 500px; }

  .brand { left: 40px; top: 414px; display: flex; align-items: center; gap: 10px;
    font-size: 24px; font-weight: 600; color: var(--ink); }
  .brand-dot { width: 26px; height: 26px; border-radius: 50%; background: var(--ink); }

  .web-note { right: 22px; top: 415px; font-size: 14.5px; color: var(--ink); white-space: nowrap; }
  .web-note strong { font-weight: 600; }

  .phone { left: 388px; top: 448px; display: flex; align-items: center; gap: 8px;
    font-size: 30px; font-weight: 700; color: var(--ink); line-height: 1; white-space: nowrap; }
  .phone svg { width: 38px; height: 38px; }

  .divider { left: 687px; top: 446px; width: 2px; height: 42px; background: var(--ink); }

  .address { left: 698px; top: 449px; display: flex; gap: 6px; }
  .address svg { width: 20px; height: 22px; margin-top: 1px; }
  .address p { font-size: 13px; font-weight: 600; color: var(--ink); line-height: 1.65; white-space: nowrap; }
</style>
</head>
<body>
  <main class="billboard">
    <svg class="sun" viewBox="0 0 1000 500" aria-hidden="true">
      <circle cx="732" cy="142" r="245" fill="var(--lime)"/>
      <circle cx="732" cy="142" r="229" fill="none" stroke="var(--white)" stroke-width="1.5"/>
    </svg>

    <div class="hero-photo" role="img" aria-label="Two puppies sitting in a wooden bath tub beside shampoo bottles, soap and folded towels"></div>

    <h1 class="headline">
      <span class="line-1">Your Best</span>
      <span class="line-2">Friend's</span>
      <span class="line-3">Best Day</span>
    </h1>

    <h2 class="services-title">Services We Offer</h2>
    <div class="services-rule"></div>

    <ul class="services">
      <li><svg viewBox="0 0 20 20"><g fill="#fff"><ellipse cx="10" cy="14" rx="5" ry="4"/><circle cx="4" cy="8" r="2.2"/><circle cx="8" cy="4.5" r="2.2"/><circle cx="12" cy="4.5" r="2.2"/><circle cx="16" cy="8" r="2.2"/></g></svg>Boarding</li>
      <li><svg viewBox="0 0 20 20"><g fill="#fff"><ellipse cx="10" cy="14" rx="5" ry="4"/><circle cx="4" cy="8" r="2.2"/><circle cx="8" cy="4.5" r="2.2"/><circle cx="12" cy="4.5" r="2.2"/><circle cx="16" cy="8" r="2.2"/></g></svg>Daycare</li>
      <li><svg viewBox="0 0 20 20"><g fill="#fff"><ellipse cx="10" cy="14" rx="5" ry="4"/><circle cx="4" cy="8" r="2.2"/><circle cx="8" cy="4.5" r="2.2"/><circle cx="12" cy="4.5" r="2.2"/><circle cx="16" cy="8" r="2.2"/></g></svg>Grooming</li>
      <li><svg viewBox="0 0 20 20"><g fill="#fff"><ellipse cx="10" cy="14" rx="5" ry="4"/><circle cx="4" cy="8" r="2.2"/><circle cx="8" cy="4.5" r="2.2"/><circle cx="12" cy="4.5" r="2.2"/><circle cx="16" cy="8" r="2.2"/></g></svg>Training</li>
    </ul>

    <svg class="footer-bands" viewBox="0 0 1000 500" aria-hidden="true">
      <polygon points="318,404 1000,404 1000,500 368,500" fill="var(--lime)"/>
      <polygon points="0,367 299,367 368,500 0,500" fill="var(--white)"/>
    </svg>

    <div class="brand"><span class="brand-dot"></span>Bright Meadow</div>

    <p class="web-note">You can find more information our website at <strong>pawplayhub@mailnest.example</strong></p>

    <div class="phone">
      <svg viewBox="0 0 40 40" aria-hidden="true">
        <circle cx="20" cy="20" r="19" fill="var(--ink)"/>
        <path d="M14 11c1-1 2.5-1 3 0l2 4c.4 1 0 1.8-.8 2.4l-1 .8c1 2.4 2.8 4.2 5.2 5.2l.8-1c.6-.8 1.4-1.2 2.4-.8l4 2c1 .5 1 2 0 3l-1.6 1.6c-1.4 1.4-4 1.4-7-.4-3.4-2-6-4.6-8-8-1.8-3-1.8-5.600-.4-7z" fill="var(--lime)"/>
      </svg>
      (555) 204-7731
    </div>

    <div class="divider"></div>

    <div class="address">
      <svg viewBox="0 0 20 22" aria-hidden="true">
        <path d="M10 1a8 8 0 0 0-8 8c0 5.5 8 12 8 12s8-6.5 8-12a8 8 0 0 0-8-8z" fill="var(--ink)"/>
        <circle cx="10" cy="9" r="3" fill="var(--lime)"/>
      </svg>
      <p>Bright Meadow Canine Activity Center<br>48 Orchard Lane, Maple Grove, IA 50000</p>
    </div>
  </main>
</body>
</html>
```